Postcard Design Project

Underground fencing for dogs (Invisible dog fencing) a postcard for my customers
"Keeping in touch with them" offering them $25.00 service call/ $75.00 install I My Logo on my truck/paper work is the Girl & Dog touching noises.

Fencing

```html
<!DOCTYPE html>
<html lang="en">
<head>
<meta charset="utf-8">
<title>Harborline Pet Containment Postcard</title>
<link rel="stylesheet" href="https://fonts.googleapis.com/css2?family=Oswald:wght@400;500;600&family=Montserrat:wght@800&display=swap">
<style>
  :root {
    --teal: #1d9a84;
    --teal-dark: #0f6b5c;
    --orange: #f0711f;
    --charcoal: #2b2b2b;
    --grey-text: #4a4a4a;
    --paper: #ffffff;
    --backdrop: #e9e9e9;
    --line: #9a9a9a;
  }
  * { box-sizing: border-box; margin: 0; padding: 0; }
  html, body { width: 689px; height: 1200px; overflow: hidden; }
  body {
    background: var(--backdrop);
    font-family: "Oswald", "Arial Narrow", sans-serif;
    position: relative;
  }
  .postcard {
    position: absolute;
    left: 44px;
    width: 600px;
    height: 386px;
    background: var(--paper);
    overflow: hidden;
    box-shadow: 0 4px 14px rgba(0,0,0,.18);
  }
  .postcard--front { top: 140px; }
  .postcard--back { top: 620px; }

  /* Front */
  .front-shapes { position: absolute; inset: 0; }
  .priority-bar {
    position: absolute; left: 0; top: 0; width: 330px; height: 54px;
    background: var(--orange);
    clip-path: polygon(0 0, 100% 0, 95% 100%, 0 100%);
    color: #fff; font-weight: 500; font-size: 21px;
    line-height: 54px; padding-left: 22px;
  }
  .headline-main {
    position: absolute; left: 19px; top: 58px;
    font-family: "Montserrat", "Arial Black", sans-serif;
    font-weight: 800; font-size: 47px; letter-spacing: 1px;
    color: var(--teal);
  }
  .headline-sub {
    position: absolute; left: 19px; top: 110px;
    font-weight: 600; font-size: 31px; color: var(--orange); line-height: 1;
  }
  .headline-sub span { font-size: 20px; color: var(--grey-text); font-weight: 500; margin-left: 4px; }
  .offer-box {
    position: absolute; left: 20px; top: 163px; width: 213px; height: 168px;
    border: 1.5px dashed var(--line);
  }
  .offer-box__title {
    position: absolute; left: 50%; top: -14px; transform: translateX(-50%);
    background: #fff; padding: 0 6px;
    font-size: 20px; font-weight: 500; color: var(--charcoal); white-space: nowrap;
  }
  .offer-ticket {
    position: absolute; left: 16px; width: 178px; height: 62px;
    background: var(--teal); color: #fff; text-align: center;
    box-shadow: 0 4px 0 var(--teal-dark);
  }
  .offer-ticket::before {
    content: ""; position: absolute; inset: 4px; border: 1px dashed rgba(255,255,255,.7);
  }
  .offer-ticket--service { top: 14px; }
  .offer-ticket--install { top: 91px; }
  .offer-ticket__price { font-size: 31px; font-weight: 500; line-height: 42px; display: block; }
  .offer-ticket__label {
    font-size: 12px; line-height: 14px; display: block;
    border-top: 1px solid rgba(255,255,255,.8); margin: 0 14px;
  }
  .contact-bar {
    position: absolute; left: 0; width: 340px; height: 48px;
    background: var(--charcoal); display: flex; align-items: center;
  }
  .postcard--front .contact-bar { top: 338px; }
  .postcard--back .contact-bar { top: 259px; width: 312px; height: 54px; }
  .brand {
    display: flex; align-items: center; gap: 8px; padding: 0 10px 0 14px;
    border-right: 1px solid #888; height: 30px;
  }
  .brand__mark { width: 30px; height: 30px; background: var(--orange); flex: none; }
  .brand__name { font-size: 12px; font-weight: 600; color: var(--orange); line-height: 1.05; text-transform: uppercase; }
  .contact { padding-left: 10px; line-height: 1.1; }
  .contact__cta { font-size: 13px; font-weight: 600; color: var(--orange); display: block; }
  .contact__phone { font-size: 13px; color: #fff; display: block; }

  /* Back */
  .back-banner {
    position: absolute; left: 0; top: 0; width: 272px; height: 76px;
    background: var(--teal); padding: 10px 0 0 16px;
    color: #fff; font-size: 17px; line-height: 19px; font-weight: 500; text-transform: uppercase;
  }
  .back-banner .muted { color: #1f3d37; font-weight: 400; }
  .experience {
    position: absolute; left: 16px; top: 86px; font-size: 26px; font-weight: 600;
    color: var(--orange); line-height: 1;
  }
  .experience-sub {
    position: absolute; left: 16px; top: 117px; font-size: 13px; color: var(--teal);
    text-transform: uppercase;
  }
  .experience-sub small { text-transform: none; color: var(--grey-text); font-size: 11px; }
  .service-photos {
    position: absolute; left: 0; top: 140px; width: 290px; height: 119px;
    background: linear-gradient(180deg, #ffffff 0%, #e7e2da 40%, #b8b39a 100%);
  }
  .stamp-box {
    position: absolute; left: 507px; top: 17px; width: 74px; height: 65px;
    border: 1.5px solid var(--grey-text);
  }
  .address-line {
    position: absolute; left: 375px; width: 205px; height: 1px; background: var(--line);
  }
</style>
</head>
<body>

<section class="postcard postcard--front" aria-label="Postcard front">
  <div class="contact-bar">
    <div class="brand">
      <span class="brand__mark"></span>
      <span class="brand__name">Harborline<br>Pet Containment</span>
    </div>
    <div class="contact">
      <span class="contact__cta">FREE ESTIMATES!</span>
      <span class="contact__phone">(555) 014-2870</span>
    </div>
  </div>
  <svg class="front-shapes" viewBox="0 0 600 386" width="600" height="386">
    <defs>
      <linearGradient id="parkGradient" x1="0" y1="0" x2="0" y2="1">
        <stop offset="0" stop-color="#3f5e2c"/>
        <stop offset=".5" stop-color="#7fa35a"/>
        <stop offset="1" stop-color="#6c9a3e"/>
      </linearGradient>
    </defs>
    <polygon points="356,0 600,0 600,386 356,386 283,190" fill="url(#parkGradient)" role="img" aria-label="Photo of a smiling man crouching on grass beside a white retriever"/>
    <polygon points="317,0 356,0 283,190 250,190" fill="var(--teal)"/>
    <polygon points="250,190 283,190 356,386 317,386" fill="var(--teal-dark)"/>
  </svg>
  <div class="priority-bar">Your Pet’s Safety is Our Priority</div>
  <div class="headline-main">KEEPING</div>
  <div class="headline-sub">IN TOUCH<span>WITH THEM</span></div>
  <div class="offer-box">
    <div class="offer-box__title">You Get</div>
    <div class="offer-ticket offer-ticket--service">
      <span class="offer-ticket__price">$25.00</span>
      <span class="offer-ticket__label">SERVICE CALLS</span>
    </div>
    <div class="offer-ticket offer-ticket--install">
      <span class="offer-ticket__price">$75.00</span>
      <span class="offer-ticket__label">INSTALLATION</span>
    </div>
  </div>
</section>

<section class="postcard postcard--back" aria-label="Postcard back">
  <div class="service-photos" role="img" aria-label="Round photos of dog training, a fenced home yard and a technician with a dog"></div>
  <svg class="front-shapes" viewBox="0 0 600 386" width="600" height="386" aria-hidden="true">
    <path d="M272 0 C262 60, 250 110, 276 170 C300 230, 340 270, 348 313 L334 313 C322 275, 286 235, 262 175 C238 115, 252 60, 262 0 Z" fill="var(--orange)"/>
  </svg>
  <div class="back-banner">
    Veterinarian Approved<br>
    <span class="muted">Underground Fencing &amp;</span><br>
    Training for Your Dog
  </div>
  <div class="experience">MOST EXPERIENCED</div>
  <div class="experience-sub">In Fairfield County <small>Since 1995</small></div>
  <div class="contact-bar">
    <div class="brand">
      <span class="brand__mark"></span>
      <span class="brand__name">Harborline<br>Pet Containment</span>
    </div>
    <div class="contact">
      <span class="contact__cta">FREE ESTIMATES!</span>
      <span class="contact__phone">(555) 014-2870</span>
    </div>
  </div>
  <div class="stamp-box"></div>
  <div class="address-line" style="top:236px"></div>
  <div class="address-line" style="top:274px"></div>
  <div class="address-line" style="top:313px"></div>
</section>

</body>
</html>
```